Microlight Aircraft Website Project

Need a website designed, or at least a template made, that my web programmer can work with here. We are a new manufacturer of microlight aircraft & powered hang gliders. Our company name is Brisk Fern. We manufacture portable utility aircraft in the Light Sport category (formerly known as Ultralights or Microlights). Our particular design is a 2-seat powered hang glider and caters to those who want to go explore the backcountry. We are not necessarily aviation nuts, but more into the development of a flying utility vehicle for extreme exploration and expeditions. We have been importing these aircraft from 3 countries for 15 years and have supplied over 200 expedition-quality aircraft world-wide. We are now manufacturing here in the US.

Industry/Entity Type

Manufacturer

Coding

Coded - Design and coding required

```html
<!DOCTYPE html>
<html lang="en">
<head>
<meta charset="utf-8">
<title>Brisk Fern – Microlight Aircraft Specialist</title>
<link href="https://fonts.googleapis.com/css2?family=Arimo:wght@400;700&family=Open+Sans:ital,wght@0,400;0,600;0,700;1,400&display=swap" rel="stylesheet">
<style>
:root{
  --navy:#0b4c9a;
  --navy-deep:#083f84;
  --sky:#1db2e4;
  --ink:#222;
  --text:#666;
  --muted:#888;
  --light:#eef1f4;
  --white:#fff;
  --line:#dcdcdc;
}
*{box-sizing:border-box;margin:0;padding:0}
html,body{width:1200px;height:2761px;overflow:hidden}
body{font-family:"Open Sans",sans-serif;color:var(--text);background:var(--white);position:relative}
.abs{position:absolute}
h2.section-title{position:absolute;left:0;width:1200px;text-align:center;font-family:"Arimo",sans-serif;font-weight:700;font-size:25px;color:var(--ink);text-transform:uppercase}
h2.section-title span{color:var(--navy)}
.read-more{font-family:"Open Sans",sans-serif;font-weight:700;font-size:12px;color:var(--sky);text-transform:uppercase;position:absolute}

/* header */
.site-header{position:absolute;top:0;left:0;width:1200px;height:88px;background:var(--white);border-top:4px solid var(--navy-deep);z-index:3}
.brand{position:absolute;left:114px;top:0;width:166px;height:132px;background:var(--white);display:flex;align-items:center;justify-content:center;font-family:"Arimo",sans-serif;font-weight:700;font-size:20px;color:var(--navy);letter-spacing:1px;z-index:4}
.contact-top{position:absolute;top:16px;display:flex;align-items:center;gap:10px;font-size:13px;color:var(--ink)}
.contact-top svg{width:28px;height:28px}
.main-nav{position:absolute;top:58px;right:100px;display:flex;gap:25px;font-family:"Arimo",sans-serif;font-weight:700;font-size:13px;color:var(--ink)}
.main-nav .active{color:var(--sky)}

/* hero */
.hero{position:absolute;top:88px;left:0;width:1200px;height:442px;background:linear-gradient(180deg,#7c8f88 0%,#5f7556 45%,#7a8a4e 75%,#8c9356 100%)}
.hero h1{position:absolute;top:140px;width:1200px;text-align:center;font-family:"Arimo",sans-serif;font-weight:700;font-size:45px;color:var(--white);text-shadow:0 2px 4px rgba(0,0,0,.5)}
.hero p{position:absolute;top:194px;width:1200px;text-align:center;font-size:23px;color:var(--white);text-shadow:0 1px 3px rgba(0,0,0,.5)}
.hero .btn{position:absolute;left:479px;top:243px;width:242px;height:50px;background:var(--sky);border:2px solid var(--white);color:var(--white);font-weight:600;font-size:15px;display:flex;align-items:center;justify-content:center}
.dots{position:absolute;top:387px;left:533px;display:flex;gap:7px}
.dots i{display:block;width:28px;height:5px;background:var(--white);border-radius:3px}
.dots i.on{background:var(--sky)}

/* welcome */
.welcome{position:absolute;top:530px;left:0;width:1200px;height:478px}
.welcome .intro{position:absolute;top:96px;left:230px;width:740px;text-align:center;font-size:12px;line-height:23px}
.feature{position:absolute;top:170px;width:240px;text-align:center}
.feature .ring{width:122px;height:122px;margin:0 auto;border-radius:50%;border:2px solid var(--navy);padding:5px}
.feature .ring div{width:100%;height:100%;border-radius:50%;background:var(--navy);display:flex;align-items:center;justify-content:center}
.feature h3{margin-top:20px;font-family:"Arimo",sans-serif;font-size:18px;color:var(--ink);font-weight:700}
.feature p{margin-top:12px;font-size:12px;line-height:22px;padding:0 12px}
.feature .read-more{position:static;display:block;margin-top:18px}

/* range */
.range{position:absolute;top:1008px;left:0;width:1200px;height:482px;background:var(--light)}
.card{position:absolute;top:96px;width:316px}
.card .photo{height:206px;border:4px solid var(--white);box-shadow:0 0 0 1px var(--line)}
.card h3{margin-top:24px;font-family:"Arimo",sans-serif;font-size:17px;font-weight:700;color:var(--ink)}
.card p{margin-top:10px;font-size:12px;line-height:22px}
.card .read-more{position:static;display:block;margin-top:8px}
.arrow{position:absolute;width:42px;height:42px;border-radius:50%;background:rgba(190,195,200,.8);display:flex;align-items:center;justify-content:center}

/* testimonials */
.testimonials{position:absolute;top:1490px;left:0;width:1200px;height:227px;background:var(--sky)}
.testimonials h2{position:absolute;top:28px;width:1200px;text-align:center;font-family:"Arimo",sans-serif;font-size:24px;font-weight:700;color:var(--white)}
.quote-bubble{position:absolute;left:147px;top:84px;width:97px;height:97px;border-radius:50%;background:#e3e3e3;display:flex;align-items:center;padding-left:14px;font-family:Georgia,serif;font-size:90px;color:#bdbdbd;line-height:1}
.client-photo{position:absolute;left:218px;top:79px;width:110px;height:110px;border-radius:50%;background:linear-gradient(180deg,#d9dde2,#8a93a0);border:4px solid var(--white)}
.testimonials blockquote{position:absolute;left:362px;top:82px;width:690px;font-style:italic;font-size:13px;line-height:27px;color:var(--white)}
.testimonials cite{position:absolute;left:362px;top:176px;font-style:normal;font-weight:700;font-size:13px;color:var(--white)}

/* about & news */
.about-news{position:absolute;top:1717px;left:0;width:1200px;height:451px}
.col-title{position:absolute;top:46px;font-family:"Arimo",sans-serif;font-weight:700;font-size:25px;color:var(--ink)}
.col-title span{color:var(--navy)}
.about-photo{position:absolute;left:98px;top:105px;width:375px;height:184px;background:linear-gradient(160deg,#3f7fc6,#5b96d2);border:4px solid var(--white);box-shadow:0 0 0 1px var(--line)}
.about-text{position:absolute;left:98px;top:306px;width:380px;font-size:12px;line-height:22px}
.news-item{position:absolute;left:526px;width:576px;height:120px}
.news-item .thumb{position:absolute;left:0;top:0;width:111px;height:101px;border:4px solid var(--white);box-shadow:0 0 0 1px var(--line)}
.news-item h4{position:absolute;left:135px;top:4px;font-family:"Arimo",sans-serif;font-size:13px;font-weight:700;color:var(--ink)}
.news-item .date{position:absolute;left:135px;top:29px;font-size:12px;color:var(--navy);display:flex;gap:8px;align-items:center}
.news-item p{position:absolute;left:135px;top:55px;width:440px;font-size:12px;line-height:22px}
.news-rule{position:absolute;left:526px;width:576px;height:1px;background:var(--line)}

/* gallery */
.gallery{position:absolute;top:2168px;left:0;width:1200px;height:288px;background:var(--light)}
.gallery .shot{position:absolute;top:99px;width:186px;height:140px;border:4px solid var(--white);box-shadow:0 0 0 1px var(--line)}

/* footer */
.site-footer{position:absolute;top:2456px;left:0;width:1200px;height:305px;background:var(--navy)}
.footer-brand{position:absolute;left:98px;top:96px;font-family:"Arimo",sans-serif;font-weight:700;font-size:30px;color:var(--white);letter-spacing:1px}
.footer-col h5{position:absolute;top:40px;font-family:"Arimo",sans-serif;font-weight:700;font-size:15px;color:var(--white);text-transform:uppercase}
.footer-links{position:absolute;left:401px;top:80px;list-style:none;font-size:12px;line-height:18.6px;color:var(--white)}
.newsletter p{position:absolute;left:578px;top:80px;width:270px;font-size:12px;line-height:21px;color:var(--white)}
.newsletter .field{position:absolute;left:578px;top:120px;width:263px;height:35px;background:var(--white);font-size:11px;color:#777;padding:10px 12px}
.newsletter .btn{position:absolute;left:578px;top:168px;width:101px;height:35px;border:2px solid var(--white);color:var(--white);font-weight:700;font-size:12px;display:flex;align-items:center;justify-content:center}
.contact-list div{position:absolute;left:909px;display:flex;gap:16px;font-size:12px;line-height:20px;color:var(--white)}
.contact-list svg{flex:none;margin-top:3px}
.footer-rule{position:absolute;left:0;top:234px;width:1200px;height:1px;background:rgba(255,255,255,.2)}
.copyright{position:absolute;left:98px;top:260px;font-size:11px;color:var(--white)}
.social{position:absolute;left:949px;top:250px;display:flex;gap:8px}
.social i{display:block;width:34px;height:34px;border:2px solid var(--white);border-radius:50%}
</style>
</head>
<body>

<header class="site-header">
  <div class="brand">BRISK FERN</div>
  <div class="contact-top" style="left:792px">
    <svg viewBox="0 0 28 28"><circle cx="14" cy="14" r="12.5" fill="none" stroke="#1db2e4" stroke-width="2"/><path d="M10 8l3 0 1 4-2 1.5c1 2 2.5 3.5 4.5 4.5L18 16l4 1v3c-7 0-12-5-12-12z" fill="#1db2e4" transform="translate(-1,0)"/></svg>
    <span>1 800 555 0142</span>
  </div>
  <div class="contact-top" style="left:944px">
    <svg viewBox="0 0 28 28"><circle cx="14" cy="14" r="12.5" fill="none" stroke="#1db2e4" stroke-width="2"/><rect x="8" y="9.5" width="12" height="9" fill="#1db2e4"/><path d="M8 9.5l6 5 6-5" fill="none" stroke="#fff" stroke-width="1.3"/></svg>
    <span>info@briskfern.com</span>
  </div>
  <nav class="main-nav">
    <span class="active">HOME</span><span>ABOUT US</span><span>OUR AIRCRAFTS</span><span>DEALERS</span><span>GALLERY</span><span>NEWS</span><span>CONTACT US</span>
    <svg width="13" height="13" viewBox="0 0 13 13"><circle cx="5.5" cy="5.5" r="4" fill="none" stroke="#222" stroke-width="2"/><path d="M8.5 8.5l3.5 3.5" stroke="#222" stroke-width="2"/></svg>
  </nav>
</header>

<section class="hero" role="img" aria-label="Powered hang glider taking off over a grass airfield lined with trees">
  <h1>MICROLIGHT AIRCRAFT SPECIALIST</h1>
  <p>We are manufacturer of microlight aircraft &amp; powered hang gliders</p>
  <div class="btn">GET MORE INFORMATION</div>
  <div class="dots"><i class="on"></i><i></i><i></i><i></i></div>
</section>

<section class="welcome">
  <h2 class="section-title" style="top:48px">Welcome to <span>Brisk Fern</span></h2>
  <p class="intro">We are microlight aircraft specialist. We are manufacturer of microlight aircraft &amp; powered hang gliders. Our particular design is a 2-seat powered hang glider and caters to those who want to go explore the country.</p>

  <div class="feature" style="left:86px">
    <div class="ring"><div><svg width="48" height="48" viewBox="0 0 48 48" fill="#fff"><circle cx="18" cy="26" r="9"/><circle cx="18" cy="26" r="3.5" fill="#0b4c9a"/><path d="M16 13h4v4h-4zM16 35h4v4h-4zM5 24h4v4H5zM27 24h4v4h-4z"/><circle cx="34" cy="14" r="6"/><circle cx="34" cy="14" r="2.2" fill="#0b4c9a"/><circle cx="35" cy="34" r="5"/><circle cx="35" cy="34" r="1.8" fill="#0b4c9a"/></svg></div></div>
    <h3>Latest Technology</h3>
    <p>Nemo enim ipsam voluptatem quia voluptas sit aspernatur aut odit aut fug sed quia consequuntur</p>
    <span class="read-more">Read More &gt;&gt;</span>
  </div>
  <div class="feature" style="left:347px">
    <div class="ring"><div><svg width="48" height="48" viewBox="0 0 48 48" fill="none" stroke="#fff" stroke-width="2.5"><rect x="4" y="18" width="10" height="10" fill="#fff"/><path d="M14 23h8M22 10v26M22 10h6M22 23h6M22 36h6M34 38v6"/><rect x="28" y="6" width="14" height="8" fill="#fff"/><rect x="28" y="19" width="14" height="8" fill="#fff"/><rect x="28" y="32" width="14" height="8" fill="#fff"/></svg></div></div>
    <h3>Exciting Range</h3>
    <p>Nemo enim ipsam voluptatem quia voluptas sit aspernatur aut odit aut fug sed quia consequuntur</p>
    <span class="read-more">Read More &gt;&gt;</span>
  </div>
  <div class="feature" style="left:609px">
    <div class="ring"><div><svg width="48" height="48" viewBox="0 0 48 48"><path d="M38 8a9 9 0 0 0-11 11L9 37a3 3 0 0 0 4 4l18-18a9 9 0 0 0 11-11l-5 5-4-1-1-4z" fill="#fff"/></svg></div></div>
    <h3>Manufacture</h3>
    <p>Nemo enim ipsam voluptatem quia voluptas sit aspernatur aut odit aut fug sed quia consequuntur</p>
    <span class="read-more">Read More &gt;&gt;</span>
  </div>
  <div class="feature" style="left:870px">
    <div class="ring"><div><svg width="48" height="48" viewBox="0 0 48 48" fill="none" stroke="#fff" stroke-width="3"><path d="M18 32c0-6-6-8-6-15a12 12 0 0 1 24 0c0 7-6 9-6 15z"/><path d="M19 37h10M20 42h8"/></svg></div></div>
    <h3>Expertise</h3>
    <p>Nemo enim ipsam voluptatem quia voluptas sit aspernatur aut odit aut fug sed quia consequuntur</p>
    <span class="read-more">Read More &gt;&gt;</span>
  </div>
</section>

<section class="range">
  <h2 class="section-title" style="top:46px">Our <span>Aircraft Range</span></h2>
  <div class="card" style="left:98px">
    <div class="photo" role="img" aria-label="Red-winged powered hang glider flying low over a dry field" style="background:linear-gradient(180deg,#c9d6e2 0%,#b9b3a8 55%,#8a6f52 100%)"></div>
    <h3>2-seat powered hang glider</h3>
    <p>Ut enim ad minima veniam, quis nostrum exercitation em ullam corporis suscipit laboriosam, nisi ut aliquid ea commodi consequatur.</p>
    <span class="read-more">Read More &gt;&gt;</span>
  </div>
  <div class="card" style="left:442px">
    <div class="photo" role="img" aria-label="Blue-winged powered hang glider against a clear blue sky" style="background:linear-gradient(180deg,#7fb4e6,#a9cdee)"></div>
    <h3>2-seat powered hang glider</h3>
    <p>Ut enim ad minima veniam, quis nostrum exercitation em ullam corporis suscipit laboriosam, nisi ut aliquid ea commodi consequatur.</p>
    <span class="read-more">Read More &gt;&gt;</span>
  </div>
  <div class="card" style="left:782px">
    <div class="photo" role="img" aria-label="Powered hang glider trike seen from below against a blue sky" style="background:linear-gradient(180deg,#8fbbe0,#c4dbef)"></div>
    <h3>2-seat powered hang glider</h3>
    <p>Ut enim ad minima veniam, quis nostrum exercitation em ullam corporis suscipit laboriosam, nisi ut aliquid ea commodi consequatur.</p>
    <span class="read-more">Read More &gt;&gt;</span>
  </div>
  <div class="arrow" style="left:67px;top:178px"><svg width="12" height="16" viewBox="0 0 12 16"><path d="M9 2L3 8l6 6" fill="none" stroke="#fff" stroke-width="2"/></svg></div>
  <div class="arrow" style="left:1078px;top:178px"><svg width="12" height="16" viewBox="0 0 12 16"><path d="M3 2l6 6-6 6" fill="none" stroke="#fff" stroke-width="2"/></svg></div>
</section>

<section class="testimonials">
  <h2>CLIENT TESTIMONIALS</h2>
  <svg class="abs" style="left:98px;top:105px" width="12" height="18" viewBox="0 0 12 18"><path d="M10 2L3 9l7 7" fill="none" stroke="#fff" stroke-width="2"/></svg>
  <svg class="abs" style="left:1088px;top:105px" width="12" height="18" viewBox="0 0 12 18"><path d="M2 2l7 7-7 7" fill="none" stroke="#fff" stroke-width="2"/></svg>
  <div class="quote-bubble">“</div>
  <div class="client-photo" role="img" aria-label="Portrait of the client"></div>
  <blockquote>It is a long established fact that a reader will be distracted by the readable content of a page when looking at its layout. The point of using Lorem Ipsum is that it has a more-or-less normal distribution of letters, as opposed to using 'Content here, content here', making it look like readable English.</blockquote>
  <cite>- DANA MILLER</cite>
</section>

<section class="about-news">
  <h2 class="col-title" style="left:98px">ABOUT <span>BRISK FERN</span></h2>
  <div class="about-photo" role="img" aria-label="Yellow-green winged powered hang glider banking in a blue sky"></div>
  <p class="about-text">At vero eos et accusamus et iusto odio dignissimos ducimus qui bla nditiis praesentium voluptatum deleniti atque corrupti quos dolore set quas molestias excepturi sint.</p>
  <span class="read-more" style="left:98px;top:389px">Read More &gt;&gt;</span>

  <h2 class="col-title" style="left:521px">OUR <span>NEWS</span></h2>
  <article class="news-item" style="top:101px">
    <div class="thumb" role="img" aria-label="Yellow powered hang glider parked on grass" style="background:linear-gradient(180deg,#b7c6a0,#6f8a4a)"></div>
    <h4>AT VERO EOS ET ACCUSAMUS ET IUSTO ODIO DIG</h4>
    <div class="date"><svg width="12" height="12" viewBox="0 0 12 12"><rect x="1" y="2" width="10" height="9" fill="#0b4c9a"/><rect x="2.5" y="5" width="7" height="4.5" fill="#fff"/></svg>05/03/2016</div>
    <p>Nemo enim ipsam voluptatem quia voluptas sit aspernatur aut odit aut fugit, sed quia consequuntur..</p>
  </article>
  <div class="news-rule" style="top:221px"></div>
  <article class="news-item" style="top:239px">
    <div class="thumb" role="img" aria-label="Green powered hang glider on a grass field" style="background:linear-gradient(180deg,#c2cfae,#5f8a3e)"></div>
    <h4>AT VERO EOS ET ACCUSAMUS ET IUSTO ODIO DIG</h4>
    <div class="date"><svg width="12" height="12" viewBox="0 0 12 12"><rect x="1" y="2" width="10" height="9" fill="#0b4c9a"/><rect x="2.5" y="5" width="7" height="4.5" fill="#fff"/></svg>05/03/2016</div>
    <p>Nemo enim ipsam voluptatem quia voluptas sit aspernatur aut odit aut fugit, sed quia consequuntur..</p>
  </article>
  <div class="news-rule" style="top:359px"></div>
  <span class="read-more" style="left:526px;top:389px">View More &gt;&gt;</span>
</section>

<section class="gallery">
  <h2 class="section-title" style="top:42px">Our <span>Gallery</span></h2>
  <div class="shot" role="img" aria-label="Red-winged trike in flight" style="left:101px;background:linear-gradient(180deg,#9cc3e8,#c8def2)"></div>
  <div class="shot" role="img" aria-label="Blue-winged trike in flight" style="left:303px;background:linear-gradient(180deg,#8ab9e6,#b8d5ef)"></div>
  <div class="shot" role="img" aria-label="Yellow trikes lined up on an airfield" style="left:505px;background:linear-gradient(180deg,#c9cfd6,#9a9078)"></div>
  <div class="shot" role="img" aria-label="White trike seen from below in a blue sky" style="left:707px;background:linear-gradient(180deg,#3f7ec6,#6d9fd6)"></div>
  <div class="shot" role="img" aria-label="Trike parked on a grass strip under a cloudy sky" style="left:909px;background:linear-gradient(180deg,#d8dde0,#8f9b73)"></div>
  <div class="arrow" style="left:67px;top:148px"><svg width="12" height="16" viewBox="0 0 12 16"><path d="M9 2L3 8l6 6" fill="none" stroke="#fff" stroke-width="2"/></svg></div>
  <div class="arrow" style="left:1078px;top:148px"><svg width="12" height="16" viewBox="0 0 12 16"><path d="M3 2l6 6-6 6" fill="none" stroke="#fff" stroke-width="2"/></svg></div>
</section>

<footer class="site-footer">
  <div class="footer-brand">BRISK FERN</div>

  <div class="footer-col"><h5 style="left:401px">Information</h5></div>
  <ul class="footer-links">
    <li>Home</li><li>About us</li><li>Our Aircrafts</li><li>Dealers</li><li>Gallery</li><li>News</li><li>Contact Us</li>
  </ul>

  <div class="footer-col newsletter">
    <h5 style="left:578px">Newsletter</h5>
    <p>Register your email address to get information about us</p>
    <div class="field">Email Address</div>
    <div class="btn">SUBSCRIBE</div>
  </div>

  <div class="footer-col contact-list">
    <h5 style="left:909px">Contact Us</h5>
    <div style="top:84px"><svg width="10" height="14" viewBox="0 0 10 14"><path d="M5 0a5 5 0 0 0-5 5c0 4 5 9 5 9s5-5 5-9a5 5 0 0 0-5-5z" fill="#fff"/><circle cx="5" cy="5" r="2" fill="#0b4c9a"/></svg><span>1250 Meadow Lane, Suite 20,<br>TX 75001 Plano</span></div>
    <div style="top:145px"><svg width="12" height="12" viewBox="0 0 12 12"><path d="M2 1h3l1 3-1.5 1c.7 1.4 1.7 2.4 3 3L8.5 6.5l3 1V11C5.5 11 1 6.5 1 1z" fill="#fff"/></svg><span>1 800 555 0142</span></div>
    <div style="top:183px"><svg width="13" height="10" viewBox="0 0 13 10"><rect width="13" height="10" fill="#fff"/><path d="M0 0l6.5 5L13 0" fill="none" stroke="#0b4c9a" stroke-width="1.2"/></svg><span>info@briskfern.com</span></div>
  </div>

  <div class="footer-rule"></div>
  <p class="copyright">Copyrights © 2016, Brisk Fern. All rights reserved.</p>
  <div class="social"><i></i><i></i><i></i><i></i></div>
</footer>

</body>
</html>
```